Korvix App Graphics Design

Our application promotes location based self expression via pictures and text. The primary focus of the application is on the content posted and not on the person that posted it.

We want a very clean and fresh design that evokes positive energy. Our site is unique so our design should be as well. People will reveal thoughts on our site, so the design should convey a "revealing" feel. Our site is a place where people are comfortable to freely express themselves. Colors we have in mind are blue and green hues with earth tones for background.

Our project is to design ten screens for our Korvix application at resolution of 1136-by-640 pixels:

Feed Screen
Camera Screen
Post Screen
Check In Screen
Approval Screen
Map Screen
Flag Screen
Feed Select Screen
Export Screen
Menu Screen

In the contest phase we will require only three screens to be submitted. The screens we require to be submitted are: Feed Screen; Map Screen and Camera Screen. The designer we select as the winner of the competition will then complete the project and deliver a total of the ten screens described above in the handover phase.

We have attached a document below with detailed specs of each screen, we ask for your innovation to bring these screens to life through your design.
Updates

We want to clarify one aspect regarding the VISOR: the visor needs to be transparent so that when the picture scrolls underneath it, you can still see the picture underneath the visor.

Hi Everyone,

We have noticed that some designers need clarification regarding the visor element in the feed screen.
I have attached two examples to our brief area called:
Visor Example 1 and Visor Example 2

Please note that these are not the style we are looking for but are a good example to the concept of a Transparent Visor above the feed stream. We are looking for you guys to come up with a Visor concept that is consistent with the style of the design you are submitting.

Thanks,

Bo

Target Market(s)

People 17-40 who want to share their thought about the world around them.

Industry/Entity Type

Flag

Font styles to use
Sans Serif
Other font styles liked:
• We like “Helvetica New” or “Avenir” but are flexible

Requirements
Must have
• Visor component should look innovative.

```html
<!DOCTYPE html>
<html lang="en">
<head>
<meta charset="utf-8">
<title>Korvix Camera Screen</title>
<link rel="stylesheet" href="https://fonts.googleapis.com/css2?family=Nunito+Sans:wght@800&display=swap">
<style>
  :root {
    --page-bg: #ffffff;
    --accent: #10b4e2;
    --button-face: #fafafa;
    --button-rim: #d9d6d0;
    --toolbar-bg: rgba(38, 40, 44, 0.88);
    --thumb-frame: #ebe8e3;
    --label: #ffffff;
    --chevron: #d3d3d3;
  }
  * { box-sizing: border-box; margin: 0; padding: 0; }
  html, body {
    width: 1200px; height: 1000px; overflow: hidden;
    background: var(--page-bg);
    font-family: "Nunito Sans", "Helvetica Neue", Arial, sans-serif;
  }
  .camera-screen {
    position: absolute; left: 167px; top: 164px;
    width: 866px; height: 672px; overflow: hidden;
    background: #333;
  }
  .live-view {
    position: absolute; inset: 0;
    background: linear-gradient(180deg, #e9e4ec 0%, #d9cfd8 22%, #b7b4b4 30%, #62666a 34%, #55595b 46%, #3f4043 52%, #47484b 70%, #38393c 100%);
  }
  .filter-strip {
    position: absolute; left: 0; top: 236px; width: 100%; height: 140px;
  }
  .strip-arrow {
    position: absolute; top: 24px; width: 26px; height: 64px;
  }
  .strip-arrow.prev { left: 20px; }
  .strip-arrow.next { right: 38px; }
  .filter {
    position: absolute; top: 0; width: 138px; text-align: center;
  }
  .filter-preview {
    width: 138px; height: 104px;
    border: 3px solid var(--thumb-frame); border-radius: 3px;
  }
  .filter-name {
    display: block; margin-top: 3px;
    color: var(--label); font-size: 19px; font-weight: 800; letter-spacing: 0.2px;
    text-shadow: 0 1px 2px rgba(0,0,0,0.5);
  }
  .filter.vivid   { left: 57px; }
  .filter.slate   { left: 211px; }
  .filter.instant { left: 365px; }
  .filter.pro     { left: 519px; }
  .filter.honey   { left: 673px; }
  .vivid .filter-preview   { background: linear-gradient(120deg, #f0e29a 0%, #f28bc0 40%, #3d8fd8 65%, #c52b3a 100%); }
  .slate .filter-preview   { background: linear-gradient(120deg, #f2f2f2 0%, #9a9a9a 45%, #3a3a3a 70%, #d0d0d0 100%); }
  .instant .filter-preview { background: linear-gradient(120deg, #cfc6f0 0%, #b084e0 40%, #4a6fc8 65%, #a33a6a 100%); }
  .pro .filter-preview     { background: linear-gradient(120deg, #f5e83a 0%, #ee2aa0 40%, #2a7ad8 65%, #c8102a 100%); }
  .honey .filter-preview   { background: linear-gradient(120deg, #e6d57a 0%, #b59a2c 45%, #5d4d12 70%, #c9b45a 100%); }

  .toolbar {
    position: absolute; left: 0; top: 380px; width: 100%; height: 292px;
    background: var(--toolbar-bg);
  }
  .tool {
    position: absolute; top: 25px; width: 82px; height: 82px;
    border-radius: 50%; background: var(--button-face);
    border: 4px solid var(--button-rim);
    display: flex; align-items: center; justify-content: center;
  }
  .tool svg { width: 44px; height: 44px; }
  .tool.gallery    { left: 81px; }
  .tool.exposure   { left: 192px; }
  .tool.crop       { left: 590px; }
  .tool.effects    { left: 707px; }
  .shutter {
    position: absolute; left: 347px; top: 25px; width: 177px; height: 80px;
    border-radius: 40px; background: var(--button-face);
    border: 4px solid var(--button-rim);
    display: flex; align-items: center; justify-content: center;
  }
  .shutter svg { width: 64px; height: 64px; }
</style>
</head>
<body>
  <main class="camera-screen">
    <div class="live-view" role="img" aria-label="Live camera view of a graffiti-painted wall with a ladder and a red door above dark asphalt"></div>

    <section class="filter-strip" aria-label="Filters">
      <svg class="strip-arrow prev" viewBox="0 0 26 64" aria-hidden="true"><polyline points="22,2 4,32 22,62" fill="none" stroke="var(--chevron)" stroke-width="3"/></svg>
      <div class="filter vivid"><div class="filter-preview" role="img" aria-label="Vivid filter preview"></div><span class="filter-name">Vivid</span></div>
      <div class="filter slate"><div class="filter-preview" role="img" aria-label="Black and white filter preview"></div><span class="filter-name">Slate</span></div>
      <div class="filter instant"><div class="filter-preview" role="img" aria-label="Cool instant filter preview"></div><span class="filter-name">Instant</span></div>
      <div class="filter pro"><div class="filter-preview" role="img" aria-label="High contrast filter preview"></div><span class="filter-name">Pro</span></div>
      <div class="filter honey"><div class="filter-preview" role="img" aria-label="Golden tint filter preview"></div><span class="filter-name">Honey</span></div>
      <svg class="strip-arrow next" viewBox="0 0 26 64" aria-hidden="true"><polyline points="4,2 22,32 4,62" fill="none" stroke="var(--chevron)" stroke-width="3"/></svg>
    </section>

    <nav class="toolbar" aria-label="Camera tools">
      <div class="tool gallery" title="Gallery">
        <svg viewBox="0 0 44 44"><rect x="5" y="9" width="28" height="22" rx="3" fill="var(--accent)" opacity="0.75"/><rect x="11" y="14" width="28" height="22" rx="3" fill="var(--accent)" stroke="var(--button-face)" stroke-width="2"/></svg>
      </div>
      <div class="tool exposure" title="Exposure">
        <svg viewBox="0 0 44 44" fill="none" stroke="var(--accent)" stroke-width="2.5" stroke-linecap="round">
          <circle cx="22" cy="22" r="10"/>
          <path d="M22 12 A10 10 0 0 0 22 32 Z" fill="var(--accent)" stroke="none"/>
          <line x1="22" y1="3" x2="22" y2="7"/><line x1="22" y1="37" x2="22" y2="41"/>
          <line x1="3" y1="22" x2="7" y2="22"/><line x1="37" y1="22" x2="41" y2="22"/>
          <line x1="8.5" y1="8.5" x2="11.3" y2="11.3"/><line x1="32.7" y1="32.7" x2="35.5" y2="35.5"/>
          <line x1="8.5" y1="35.5" x2="11.3" y2="32.7"/><line x1="32.7" y1="11.3" x2="35.5" y2="8.5"/>
        </svg>
      </div>
      <div class="shutter" title="Take photo">
        <svg viewBox="0 0 64 64" fill="none" stroke="var(--accent)" stroke-width="2.5">
          <circle cx="32" cy="32" r="29" fill="#bfe9f6"/>
          <circle cx="32" cy="32" r="12" fill="#ffffff"/>
          <line x1="32" y1="3" x2="44" y2="22"/><line x1="57" y1="18" x2="44" y2="38"/>
          <line x1="57" y1="46" x2="32" y2="44"/><line x1="32" y1="61" x2="20" y2="42"/>
          <line x1="7" y1="46" x2="20" y2="26"/><line x1="7" y1="18" x2="32" y2="20"/>
        </svg>
      </div>
      <div class="tool crop" title="Crop">
        <svg viewBox="0 0 44 44" fill="none" stroke="var(--accent)" stroke-width="5" stroke-linecap="square">
          <polyline points="12,4 12,32 40,32"/><polyline points="4,12 32,12 32,40"/>
        </svg>
      </div>
      <div class="tool effects" title="Effects">
        <svg viewBox="0 0 44 44" fill="var(--accent)">
          <polygon points="16,14 19,20 26,21 21,25 23,32 16,28 10,32 12,25 7,21 13,20"/>
          <line x1="20" y1="26" x2="34" y2="42" stroke="var(--accent)" stroke-width="4" stroke-linecap="round"/>
          <polygon points="26,4 27.5,7 31,7.5 28.5,10 29,13 26,11.5 23,13 23.5,10 21,7.5 24.5,7"/>
          <polygon points="36,12 37,14.5 39.5,15 37.5,16.5 38,19 36,17.5 34,19 34.5,16.5 32.5,15 35,14.5"/>
          <circle cx="34" cy="25" r="1.8"/>
        </svg>
      </div>
    </nav>
  </main>
</body>
</html>
```